Corporate Branded Documents - IT Provider - On-going work

Hi, I'm Tom a Director of Harbourline IT Care a UK Based IT & Telecoms support firm. We've been trading for 12 years now and feel its time for a lick of paint. We have a logo, website etc but would like someone to create some standard documents for us.

- A PDF Proposal Template - We currently don't send our customers proposals as we have nothing that looks good.
- A Quote Template PDF - Example Attached
- A Order Template PDF - Example Attached
- A Invoice Template PDF - Example Attached
- A Generic Document PDF - Something we can use for customer application forms, NDA Agreements, Terms & Conditions etc

Our website can be found at www.harbourlineitcare.co.uk - here you'll get a feel for our branding. I've also attached 2 example documents - as well as our currently used documents. Hopefully you guys can see why it needs improving.

We'd also like to work with someone long term, these documents are a start but we'd like to make sure all the work we do looks and feels as smart as possible, so there is plenty of additional work available.

None of these templates need to be Print ready, 99% of the time it will be viewed digitally, so high resolution designs are best

Thanks,

Tom

Target Market(s)

Corporate & Educational Customers

Industry/Entity Type

It Support

Font styles to use
Sans Serif

Colors
ec1f27
0692cd
ffffff

```html
<!DOCTYPE html>
<html lang="en">
<head>
<meta charset="utf-8">
<title>Harbourline IT Care – Invoice</title>
<link rel="stylesheet" href="https://fonts.googleapis.com/css2?family=Montserrat:wght@400;500;600;700&display=swap">
<style>
  :root {
    --brand-red: #e00c12;
    --brand-blue: #0a7fa6;
    --ink: #1d1d1d;
    --band-dark: #1c1c1c;
    --row-grey: #e7e7e7;
    --rule: #b9b9b9;
    --muted: #6a6a6a;
    --paper: #ffffff;
    --backdrop: #ececec;
  }
  * { box-sizing: border-box; margin: 0; padding: 0; }
  html, body { width: 1200px; height: 790px; overflow: hidden; }
  body {
    background: var(--backdrop);
    font-family: "Montserrat", Arial, sans-serif;
    color: var(--ink);
    position: relative;
  }
  .invoice {
    position: absolute;
    left: 333px; top: 20px;
    width: 506px; height: 710px;
    background: var(--paper);
    transform: scale(1.056);
    transform-origin: top left;
  }
  .abs { position: absolute; }

  /* header */
  .brand { left: 30px; top: 32px; display: flex; align-items: center; gap: 8px; }
  .brand-mark { width: 16px; height: 16px; background: var(--brand-red); }
  .brand-name { font-size: 15px; font-weight: 700; color: var(--brand-blue); letter-spacing: -0.3px; }
  .contact { left: 352px; font-size: 6.6px; font-weight: 600; color: var(--brand-blue); line-height: 1.35; display: flex; gap: 8px; }
  .contact svg { flex: none; }
  .contact-address { top: 22px; }
  .contact-phone { top: 55px; align-items: center; }

  /* client band */
  .client-band { left: 0; top: 105px; width: 506px; height: 133px; background: var(--band-dark); color: #fff; }
  .to-label { left: 30px; top: 18px; font-size: 7px; font-weight: 600; }
  .client-name { left: 30px; top: 30px; font-size: 15px; font-weight: 700; }
  .client-company { left: 30px; top: 48px; font-size: 9.5px; }
  .client-details { left: 30px; top: 76px; font-size: 6.3px; font-weight: 700; line-height: 1.85; }
  .invoice-no { left: 383px; top: 26px; }
  .invoice-no .label { font-size: 9.5px; }
  .invoice-no .value { font-size: 16px; font-weight: 700; letter-spacing: 0.3px; }
  .date { top: 87px; border-left: 2px solid var(--brand-red); padding-left: 6px; }
  .date .label { font-size: 7.2px; font-weight: 700; }
  .date .value { font-size: 9.5px; }
  .date-issued { left: 337px; }
  .date-due { left: 418px; }

  /* items table */
  .items-head { left: 0; top: 239px; width: 506px; height: 38px; background: var(--brand-blue); color: #fff; font-weight: 600; }
  .items-head .col-desc { left: 28px; top: 12px; font-size: 12px; }
  .items-head .col { top: 15px; font-size: 9px; }
  .row { left: 0; width: 506px; height: 38.6px; border-bottom: 1px dashed var(--rule); }
  .row.shaded { background: var(--row-grey); }
  .row .num { left: 30px; top: 16px; font-size: 8.5px; font-weight: 700; }
  .row .title { left: 55px; top: 7px; font-size: 10px; font-weight: 600; }
  .row .desc { left: 55px; top: 21px; font-size: 5.6px; color: var(--muted); }
  .row .unit-price { right: 174px; top: 16px; font-size: 8.6px; }
  .row .qty { left: 374px; width: 10px; text-align: center; top: 16px; font-size: 8.6px; font-weight: 700; }
  .row .price { right: 42px; top: 16px; font-size: 8.6px; font-weight: 700; }

  /* totals */
  .totals { left: 272px; top: 494px; width: 206px; }
  .total-line { display: flex; justify-content: space-between; padding: 0 6px; height: 24.5px; align-items: center; font-size: 8.5px; border-bottom: 1px dashed var(--rule); }
  .total-line.strong { font-weight: 700; }
  .total-line.last { border-bottom: none; }
  .grand-total { margin-top: 0; height: 38px; background: var(--brand-red); color: #fff; font-weight: 600; font-size: 12.5px; display: flex; justify-content: space-between; align-items: center; padding: 0 14px 0 12px; }
  .grand-total .amount { font-weight: 700; font-size: 13px; }

  /* payment & terms */
  .payment { left: 28px; top: 530px; font-size: 7.8px; line-height: 1.3; }
  .payment-label { display: inline-block; background: var(--brand-blue); color: #fff; font-weight: 600; font-size: 7.6px; padding: 2px 6px; margin-bottom: 3px; }
  .payment .bank { font-weight: 700; }
  .payment .gap { margin-top: 12px; }
  .payment .key-blue { color: var(--brand-blue); font-weight: 700; }
  .payment .key { font-weight: 700; }
  .terms { left: 28px; top: 624px; width: 192px; }
  .terms h3 { font-size: 7.6px; font-weight: 700; color: var(--brand-blue); margin-bottom: 2px; }
  .terms p { font-size: 5.7px; line-height: 1.3; }
  .thanks { left: 271px; top: 652px; font-size: 14px; font-weight: 700; color: var(--brand-blue); }
</style>
</head>
<body>
<main class="invoice">

  <div class="abs brand">
    <span class="brand-mark"></span>
    <span class="brand-name">Harbourline IT Care</span>
  </div>

  <div class="abs contact contact-address">
    <svg width="17" height="17" viewBox="0 0 20 20" fill="none" stroke="var(--brand-blue)" stroke-width="1.3" aria-hidden="true">
      <circle cx="9" cy="10" r="7"/><ellipse cx="9" cy="10" rx="3" ry="7"/><path d="M2 10h14M3 6.5h12M3 13.5h12"/>
      <path d="M15 1.5a3 3 0 0 1 3 3c0 2-3 5-3 5s-3-3-3-5a3 3 0 0 1 3-3z" fill="#fff"/>
    </svg>
    <span>Quayside Works,<br>22 Mill Lane,<br>Harbour Park, Leeds</span>
  </div>
  <div class="abs contact contact-phone">
    <svg width="17" height="17" viewBox="0 0 20 20" fill="none" stroke="var(--brand-blue)" stroke-width="1.3" aria-hidden="true">
      <path d="M4 2.5l3 .5 1.5 4-2 1.5a10 10 0 0 0 5 5l1.5-2 4 1.5.5 3c-1 1.5-2.5 2-4 1.5A15 15 0 0 1 2.5 7C2 5.5 2.5 3.5 4 2.5z"/>
    </svg>
    <span>0113 496 0721</span>
  </div>

  <section class="abs client-band">
    <div class="abs to-label">TO</div>
    <div class="abs client-name">Alex Carter</div>
    <div class="abs client-company">Company Name</div>
    <div class="abs client-details">
      PHONE: +012345678900<br>
      EMAIL: hello@clientmail.co.uk<br>
      ADDRESS: 123 Street Name, Suburb, City
    </div>
    <div class="abs invoice-no">
      <div class="label">Invoice No</div>
      <div class="value">78945612</div>
    </div>
    <div class="abs date date-issued">
      <div class="label">Invoice Date</div>
      <div class="value">01-01-2022</div>
    </div>
    <div class="abs date date-due">
      <div class="label">Due Date</div>
      <div class="value">01-01-2023</div>
    </div>
  </section>

  <div class="abs items-head">
    <span class="abs col-desc">Item Description</span>
    <span class="abs col" style="left:283px">Unit Price</span>
    <span class="abs col" style="left:369px">Unit</span>
    <span class="abs col" style="left:424px">Price</span>
  </div>

  <div class="abs row shaded" style="top:278px">
    <span class="abs num">1.</span><span class="abs title">Item Title</span>
    <span class="abs desc">Lorem ipsum dolor sit amet, consepiscing elit,</span>
    <span class="abs unit-price">$200.00</span><span class="abs qty">2</span><span class="abs price">$400.00</span>
  </div>
  <div class="abs row" style="top:316.6px">
    <span class="abs num">2.</span><span class="abs title">Item Title</span>
    <span class="abs desc">Lorem ipsum dolor sit amet, consepiscing elit,</span>
    <span class="abs unit-price">$150.00</span><span class="abs qty">2</span><span class="abs price">$300.00</span>
  </div>
  <div class="abs row shaded" style="top:355.2px">
    <span class="abs num">3.</span><span class="abs title">Item Title</span>
    <span class="abs desc">Lorem ipsum dolor sit amet, consepiscing elit,</span>
    <span class="abs unit-price">$600.00</span><span class="abs qty">4</span><span class="abs price">$2400.00</span>
  </div>
  <div class="abs row" style="top:393.8px">
    <span class="abs num">4.</span><span class="abs title">Item Title</span>
    <span class="abs desc">Lorem ipsum dolor sit amet, consepiscing elit,</span>
    <span class="abs unit-price">$200.00</span><span class="abs qty">6</span><span class="abs price">$1200.00</span>
  </div>
  <div class="abs row shaded" style="top:432.4px">
    <span class="abs num">5.</span><span class="abs title">Item Title</span>
    <span class="abs desc">Lorem ipsum dolor sit amet, consepiscing elit,</span>
    <span class="abs unit-price">$200.00</span><span class="abs qty">5</span><span class="abs price">$1000.00</span>
  </div>

  <div class="abs totals">
    <div class="total-line strong"><span>Sub Total</span><span>$5300.00</span></div>
    <div class="total-line"><span>Sales Tax 10%</span><span>$530.50</span></div>
    <div class="total-line last"><span>Discount</span><span>$100</span></div>
    <div class="grand-total"><span>Grand Total &nbsp;:</span><span class="amount">$5730.00</span></div>
  </div>

  <div class="abs payment">
    <span class="payment-label">Payment Methods</span>
    <div class="bank">123 Bank Ltd.</div>
    <div>A/C Name: Lorem Ipsum</div>
    <div>A/C: 1234-000-123</div>
    <div class="gap"><span class="key-blue">Online Pay:</span> email address.com</div>
    <div><span class="key">We Accept:</span> All International, Major Cards</div>
  </div>

  <div class="abs terms">
    <h3>Terms &amp; Conditions</h3>
    <p>Lorem ipsum dolor sit amet, consectetur adipiscing elit, sed do eiusmod tempor incididunt ut labore et dolore magna aliqua. Ut enim ad minim veniam, quis nostrud exercitation ullamco labo ris nisi ut aliquip ex ea commodo consequat. Duis aute irure dolor in reprehenderit in voluptate velit esse cillum dolore eu fugiat nulla pariatur. Excepteur sint occaecat cupidatat non proi-</p>
  </div>

  <div class="abs thanks">Thank you for your business!</div>

</main>
</body>
</html>
```